Business Card Design Project

We need business cards for our new business, Vantrel Optics. We specialize in aerial videography and photography via drone. Currently we are mainly focusing on real estate videography but will branch into other markets and may even host training classes for flying drones.
Updates
Cards should include:
Name
Phone Number
Email Address
Web address
We will need to customize for more than one person and would like those fields to be editable
eps file logos are uploaded now, thanks!
Target Market(s)
Real Estate Agents, hotels, rental agencies and people who have recently purchase drones
Industry/Entity Type
Videography
Font styles to use
Look and feel
Each slider illustrates characteristics of the customer's brand and the style your logo design should communicate.

```html
<!DOCTYPE html>
<html lang="en">
<head>
<meta charset="utf-8">
<title>Vantrel Optics – Business Cards</title>
<link href="https://fonts.googleapis.com/css2?family=Questrial&display=swap" rel="stylesheet">
<style>
  :root {
    --bg: #3b3b3d;
    --ink: #2a2418;
    --yellow: #ffd21c;
    --orange: #f2942e;
    --card-dark: #111112;
    --card-glow: #3a3838;
    --white: #f4f4f4;
  }
  * { box-sizing: border-box; margin: 0; padding: 0; }
  html, body { width: 1200px; height: 799px; overflow: hidden; }
  body {
    background: var(--bg);
    font-family: "Questrial", sans-serif;
    position: relative;
  }
  .card { position: absolute; overflow: hidden; background: var(--card-dark); }

  /* Vertical card */
  .card--vertical { left: 110px; top: 110px; width: 330px; height: 580px; }
  .card--vertical .info-panel {
    height: 245px;
    background: linear-gradient(180deg, var(--yellow) 0%, #fbb427 55%, var(--orange) 100%);
    padding: 46px 0 0 64px;
    border-bottom: 5px solid var(--orange);
  }
  .card--vertical .brand-panel {
    height: 335px;
    position: relative;
    background: radial-gradient(ellipse 70% 55% at 50% 95%, var(--card-glow), var(--card-dark) 70%);
  }
  .card--vertical .accent-line {
    position: absolute; left: 0; right: 0; bottom: 14px; height: 4px;
    background: linear-gradient(90deg, var(--yellow), var(--orange));
  }

  .holder-name { font-size: 27px; color: var(--ink); letter-spacing: .3px; margin-bottom: 22px; }
  .contact-list { list-style: none; }
  .contact-item {
    display: flex; align-items: flex-start; gap: 6px;
    font-size: 15.5px; color: var(--ink); line-height: 1.35; margin-bottom: 12px;
    margin-left: -20px;
  }
  .contact-item svg { flex: none; width: 13px; height: 13px; margin-top: 4px; }

  .brand {
    position: absolute; left: 0; right: 0; top: 70px;
    display: flex; flex-direction: column; align-items: center; gap: 26px;
  }
  .brand-square { width: 86px; height: 86px; background: var(--orange); }
  .brand-name { font-size: 34px; color: var(--white); letter-spacing: 2px; text-transform: uppercase; }

  /* Horizontal card */
  .card--horizontal { left: 520px; top: 230px; width: 580px; height: 330px; display: flex; }
  .card--horizontal .info-panel {
    width: 248px; height: 100%;
    background: linear-gradient(90deg, var(--yellow) 0%, #fbb427 55%, var(--orange) 100%);
    border-right: 5px solid var(--orange);
    padding: 58px 0 0 44px;
  }
  .card--horizontal .holder-name { font-size: 23px; margin-bottom: 18px; }
  .card--horizontal .contact-item { font-size: 13px; margin-bottom: 9px; margin-left: 0; }
  .card--horizontal .contact-item svg { width: 11px; height: 11px; margin-top: 3px; }
  .card--horizontal .brand-panel {
    flex: 1; position: relative;
    background: radial-gradient(ellipse 60% 70% at 50% 60%, var(--card-glow), var(--card-dark) 72%);
  }
  .card--horizontal .brand { top: 92px; gap: 20px; }
  .card--horizontal .brand-square { width: 70px; height: 70px; }
  .card--horizontal .brand-name { font-size: 30px; }
  .card--horizontal .accent-line {
    position: absolute; top: 0; bottom: 0; right: 16px; width: 4px;
    background: linear-gradient(180deg, var(--orange), var(--yellow));
  }
</style>
</head>
<body>
  <svg width="0" height="0" style="position:absolute">
    <defs>
      <symbol id="icon-pin" viewBox="0 0 16 16"><circle cx="8" cy="8" r="7" fill="none" stroke="#2a2418" stroke-width="1.5"/><path d="M8 4a2.6 2.6 0 0 0-2.6 2.6C5.4 9 8 12 8 12s2.6-3 2.6-5.4A2.6 2.6 0 0 0 8 4z" fill="#2a2418"/></symbol>
      <symbol id="icon-phone" viewBox="0 0 16 16"><circle cx="8" cy="8" r="7" fill="none" stroke="#2a2418" stroke-width="1.5"/><path d="M5.6 4.5l1.3 1.6-.7 1a5 5 0 0 0 2.6 2.6l1-.7 1.6 1.3-.8 1.1C8 11.2 4.8 8 4.6 5.3z" fill="#2a2418"/></symbol>
      <symbol id="icon-mail" viewBox="0 0 16 16"><circle cx="8" cy="8" r="7" fill="none" stroke="#2a2418" stroke-width="1.5"/><rect x="4.5" y="5.5" width="7" height="5" fill="none" stroke="#2a2418" stroke-width="1.2"/><path d="M4.5 5.5L8 8.3l3.5-2.8" fill="none" stroke="#2a2418" stroke-width="1.2"/></symbol>
      <symbol id="icon-web" viewBox="0 0 16 16"><circle cx="8" cy="8" r="7" fill="none" stroke="#2a2418" stroke-width="1.5"/><circle cx="8" cy="8" r="4" fill="none" stroke="#2a2418" stroke-width="1.1"/><path d="M4 8h8M8 4v8" stroke="#2a2418" stroke-width="1.1"/></symbol>
    </defs>
  </svg>

  <section class="card card--vertical">
    <div class="info-panel">
      <h1 class="holder-name">YOUR NAME</h1>
      <ul class="contact-list">
        <li class="contact-item"><svg><use href="#icon-pin"/></svg><span>2870 NW 88th Ave.<br>Doral, Fl. 33172</span></li>
        <li class="contact-item"><svg><use href="#icon-phone"/></svg><span>(305) 555-0142</span></li>
        <li class="contact-item"><svg><use href="#icon-mail"/></svg><span>jdoe@vantreloptics.com</span></li>
        <li class="contact-item"><svg><use href="#icon-web"/></svg><span>www.vantreloptics.com</span></li>
      </ul>
    </div>
    <div class="brand-panel">
      <div class="brand">
        <div class="brand-square"></div>
        <div class="brand-name">Vantrel Optics</div>
      </div>
      <div class="accent-line"></div>
    </div>
  </section>

  <section class="card card--horizontal">
    <div class="info-panel">
      <h2 class="holder-name">YOUR NAME</h2>
      <ul class="contact-list">
        <li class="contact-item"><svg><use href="#icon-pin"/></svg><span>2870 NW 88th Ave.<br>Doral, Fl. 33172</span></li>
        <li class="contact-item"><svg><use href="#icon-phone"/></svg><span>(305) 555-0142</span></li>
        <li class="contact-item"><svg><use href="#icon-mail"/></svg><span>jdoe@vantreloptics.com</span></li>
        <li class="contact-item"><svg><use href="#icon-web"/></svg><span>www.vantreloptics.com</span></li>
      </ul>
    </div>
    <div class="brand-panel">
      <div class="brand">
        <div class="brand-square"></div>
        <div class="brand-name">Vantrel Optics</div>
      </div>
      <div class="accent-line"></div>
    </div>
  </section>
</body>
</html>
```